PawQuarry Banner contest an ecommerce site for veterinarians

We need banners for our ecommerce site. Our site is a webstore that veterinarians can use to allow their clients to purchase items from them. Each month we have a different theme for our banners. I am looking for banners for January and February and with a refresh coming to our site could be looking at a dozen over the next year. I may potentially choose from multiple designers and increase the payment or will choose one designer for both months .

For January our theme is winter fun. We will be running a contest were people can submit a picture of their pet to our Chatterloop page enjoying the snow or keeping warm. they have a chance to win one of 5 $50 gift certificates to pawquarry. The banner should have a dog and cat and a separate one with just a cat. We will need a French and English banner. We will provide the French translation once the winner has been selected.

For February our theme is dental health. The banner should have a dog and cat and a separate one with just a cat. We will need a French and English banner. We will provide the French translation once the winner has been selected.

Target Market(s)

pet owners

Industry/Entity Type

Veterinary

Colors

Designer to choose colors to be used in the design.

Requirements
Must have
• dimensions for PQ Banner are: 710px x 280px
Nice to have
• I have attached our logo and some screen shoots of our site so you can get a feel of what it look like. you could also go to www.pawquarry.ca and see what the sign in page looks like
Should not have
• images of pet food

```html
<!DOCTYPE html>
<html lang="en">
<head>
<meta charset="utf-8">
<title>PawQuarry – Winter Pet Photo Contest</title>
<link rel="stylesheet" href="https://fonts.googleapis.com/css2?family=Parisienne&family=Crimson+Text:ital@1&family=Open+Sans:wght@600&display=swap">
<style>
  :root {
    --sky-light: #e9eef6;
    --sky-mid: #b9c6dc;
    --sky-deep: #8194b8;
    --band-white: #ffffff;
    --ink-navy: #26304a;
    --brand-red: #b4262d;
    --kitten-warm: #d99a5c;
    --kitten-cream: #f1d7b4;
    --kitten-shadow: #8a6a52;
    --tree-white: #f4f7fb;
  }
  * { margin: 0; padding: 0; box-sizing: border-box; }
  html, body { width: 1200px; height: 473px; overflow: hidden; background: #fff; }
  .banner { position: relative; width: 1200px; height: 473px; overflow: hidden; }
  .banner__art { position: absolute; inset: 0; }
  .headline {
    position: absolute; left: 42px; top: 18px;
    font-family: "Parisienne", cursive;
    font-size: 58px; line-height: 1; color: var(--ink-navy);
    transform: rotate(-2deg); transform-origin: left center;
  }
  .headline sup { font-size: 30px; vertical-align: 26px; margin-left: 2px; }
  .subline {
    position: absolute; left: 70px; top: 90px; width: 470px;
    font-family: "Crimson Text", serif; font-style: italic;
    font-size: 18px; line-height: 1.15; color: var(--ink-navy); text-align: center;
    transform: rotate(-2deg); transform-origin: left center;
  }
  .brand {
    position: absolute; left: 400px; top: 262px;
    display: flex; align-items: center; gap: 14px;
    transform: rotate(-6deg); transform-origin: left center;
  }
  .brand__mark { width: 22px; height: 22px; background: var(--brand-red); }
  .brand__name {
    font-family: "Open Sans", sans-serif; font-weight: 600;
    font-size: 52px; letter-spacing: -1px; color: var(--brand-red);
  }
</style>
</head>
<body>
  <main class="banner">
    <svg class="banner__art" width="1200" height="473" viewBox="0 0 1200 473" aria-hidden="false">
      <defs>
        <linearGradient id="sky" x1="0" y1="0" x2="0.6" y2="1">
          <stop offset="0" stop-color="var(--sky-light)"/>
          <stop offset="0.55" stop-color="var(--sky-mid)"/>
          <stop offset="1" stop-color="var(--sky-deep)"/>
        </linearGradient>
        <radialGradient id="kitten" cx="0.62" cy="0.45" r="0.6">
          <stop offset="0" stop-color="var(--kitten-cream)"/>
          <stop offset="0.45" stop-color="var(--kitten-warm)"/>
          <stop offset="1" stop-color="var(--kitten-shadow)"/>
        </radialGradient>
        <linearGradient id="trees" x1="0" y1="0" x2="0" y2="1">
          <stop offset="0" stop-color="var(--sky-deep)" stop-opacity="0"/>
          <stop offset="0.5" stop-color="var(--tree-white)" stop-opacity="0.7"/>
          <stop offset="1" stop-color="var(--tree-white)"/>
        </linearGradient>
      </defs>
      <rect class="sky" width="1200" height="473" fill="url(#sky)"/>
      <rect class="snowy-trees" role="img" aria-label="White pine tree silhouettes in falling snow"
            x="0" y="330" width="760" height="143" fill="url(#trees)"/>
      <polygon class="white-band" points="0,255 860,95 890,350 0,385" fill="var(--band-white)"/>
      <polygon class="kitten-photo" role="img" aria-label="Photo of a fluffy ginger kitten held in a hand"
               points="700,0 1200,0 1200,473 745,473" fill="url(#kitten)"/>
    </svg>

    <h1 class="headline">Chance to win 50<sup>$</sup></h1>
    <p class="subline">Participate on the contest by simpimly uploding the Pics<br>of your pets &amp; get the chance to win the $50 gifts</p>

    <div class="brand">
      <span class="brand__mark"></span>
      <span class="brand__name">pawquarry.ca</span>
    </div>
  </main>
</body>
</html>
```